K P Guard Services - Alarm and CCTV installation Flyer

Need a flyer designed that grabs the attention of potential customers, we need the price to stand out the most to grab people’s attention, whether they are residential or commercial.We are a security company based in Brentwood Essex but cover London and the home counties. here is our website to take a look at www.kpguardservices.co.uk. We want them to know we install complete alarm and Cctv systems and will keep them “safe”

Target Market(s)

residential and commercial property

Colors
f37122

Requirements
Must have
• on one side
• large clear logo - professional design
• - Intruder Alarms starting from £495 + VAT. (Big text)
• - £150 discount on installations
• *terms and conditions apply (small text)
• - Not happy with your current provider? Free of charge no obligation take over survey and quotation and up to £100 off
• - CCTV systems starting from £595 + VAT (based on 2 cameras)
• K P Guard Services are always there, always available, wherever and whenever you need us.
• Large telephone number at the bottom 01632 480913
• Address / email / website as a footer * see website for details
• on second side
• large and bold
• Are you looking to keep you and your premises safe?
• - K P Guard Services install, maintain and repair all intruder alarms, CCTV, intercom and access control
• - View, control and manage your security systems anywhere in the world
• - Feel at ease with monitoring services & police response tailored to suit you and your business
• - K P Guard can takeover any existing security system and offer maintenance checks to guarantee the best performance for you and your premises
• - K P Guard understand that being security conscious is ever increasing, protecting your property and family is a number one priority
• - Our fully insured and accredited team offer quality, safety and cost efficiency throughout the whole process
• - K P Guard Services are using the latest cloud-based technology to stay connected with your home and business 24/7
• If you are looking to improve the security in your home, office or commercial property then call a member of our team today for a free quote.
• Fully insured and accredited
• Jobrater logo and NQRB Intruder and CCTV logos
• Logo somewhere on page and
• Telephone number
• Address / email / website as footer
Nice to have
• We would like to have the text saying
• Intruder alarms installed from £495 + vat the biggest text on the page. Most likely the £495 part the largest.
• Also would like “not happy with your current provider” more obvious
• We would like use our company colours - Orange/White/black

```html
<!DOCTYPE html>
<html lang="en">
<head>
<meta charset="utf-8">
<title>K P Guard Services – Alarm and CCTV Flyer</title>
<link href="https://fonts.googleapis.com/css2?family=Arimo:wght@400;700&display=swap" rel="stylesheet">
<style>
:root{
  --orange:#f37122;
  --orange-soft:#f8a163;
  --orange-pale:#fbc59c;
  --brand-red:#e8452b;
  --black:#0b0b0b;
  --white:#ffffff;
  --ink:#1a1a1a;
  --stage:#2a2a2a;
  --photo-light:#e9ebee;
  --photo-mid:#c9ced4;
}
*{margin:0;padding:0;box-sizing:border-box}
html,body{width:1200px;height:720px;overflow:hidden;background:var(--stage);font-family:"Arimo",Arial,sans-serif;color:var(--ink)}
.sheet{position:absolute;top:20px;width:512px;height:680px;background:var(--white);overflow:hidden}
.sheet--front{left:48px}
.sheet--back{left:640px}
.abs{position:absolute}
.photo{position:absolute;background:linear-gradient(160deg,var(--photo-light),var(--photo-mid))}
.wave{position:absolute;left:0;top:0}

/* brand name */
.brand{position:absolute;text-align:center;color:var(--brand-red);font-weight:700;line-height:1}
.brand__mark{display:block;margin:0 auto 10px;background:var(--brand-red)}

/* front */
.tagline{left:88px;top:234px;width:250px;font-size:19.5px;line-height:21px;color:var(--ink)}
.switch-offer{left:0;top:332px;width:181px;height:249px;background:var(--black);color:var(--white);padding:14px 10px 0 20px}
.switch-offer__lead{font-size:17.5px;font-weight:700;line-height:19.5px}
.switch-offer__deal{margin-top:30px;font-size:14px;line-height:17px;color:var(--orange)}
.price-title{font-size:18px;color:var(--ink);white-space:nowrap}
.price-box{border:3px solid var(--orange);text-align:center;color:var(--ink)}
.price-box__from{font-size:17.5px;line-height:21px;padding-top:5px}
.price-box--alarm{left:194px;top:372px;width:157px;height:211px}
.price-box--alarm .price-box__amount{font-size:56px;line-height:58px;margin-top:2px}
.price-box--alarm .price-box__plus{font-size:46px;line-height:46px}
.price-box--alarm .price-box__vat{font-size:52px;line-height:56px}
.price-box--cctv{left:362px;top:392px;width:136px;height:192px;text-align:left;padding-left:5px}
.price-box--cctv .price-box__from{text-align:center;padding-right:5px}
.price-box--cctv .price-box__amount{font-size:21.5px;line-height:23px;margin-top:8px}

/* footer */
.footer-line{position:absolute;left:0;right:0;top:602px;height:3px;background:var(--orange)}
.phone-tab{position:absolute;left:0;top:594px;width:188px;height:86px;border-top-right-radius:26px;background:linear-gradient(90deg,var(--orange-pale),var(--orange) 85%);text-align:center}
.phone-tab svg{margin-top:14px}
.phone-tab__number{font-size:20px;font-weight:700;color:var(--ink);margin-top:2px}
.contacts{position:absolute;left:198px;top:611px;list-style:none;font-size:10px;font-weight:700}
.contacts li{display:flex;align-items:center;gap:9px;height:21px}

/* back */
.headline-panel{left:130px;top:42px;width:382px;height:122px;background:rgba(255,255,255,.82);padding:22px 0 0 25px}
.headline{font-size:30px;font-weight:700;line-height:33px;color:var(--black)}
.points{position:absolute;list-style:none;font-size:11.5px;line-height:13px}
.points li{position:absolute;padding-left:10px}
.points li::before{content:"";position:absolute;left:0;top:1px;border-left:8px solid var(--orange);border-top:6px solid transparent;border-bottom:6px solid transparent}
.points--left{left:28px;width:240px}
.points--right{left:268px;width:232px}
.cta{left:274px;top:514px;width:238px;height:72px;background:linear-gradient(90deg,var(--orange-soft),var(--orange-pale));padding:6px 8px;font-size:11.8px;line-height:13.5px}
.badge{position:absolute;background:#f1f1f1;border:1px solid #9a9a9a}
.badge-label{position:absolute;font-size:5px;text-align:center;color:#333}
</style>
</head>
<body>

<!-- Front side -->
<section class="sheet sheet--front">
  <div class="photo" style="left:0;top:0;width:512px;height:300px" role="img" aria-label="Alarm keypad being pressed beside a bullet security camera on a light wall"></div>
  <svg class="wave" width="512" height="330" viewBox="0 0 512 330" aria-hidden="true">
    <path d="M0 260 C150 220 330 200 512 212 L512 330 L0 330 Z" fill="var(--orange)"/>
    <path d="M0 266 C150 228 330 212 512 226 L512 330 L0 330 Z" fill="var(--white)"/>
  </svg>
  <div class="photo" style="left:348px;top:190px;width:152px;height:156px;border-radius:12px;background:linear-gradient(150deg,#3a3f47,#1e2228)" role="img" aria-label="Two smartphones showing a security system control app"></div>

  <div class="brand" style="left:170px;top:66px;width:200px;font-size:32px">
    <span class="brand__mark" style="width:58px;height:58px"></span>K P GUARD<br>SERVICES
  </div>

  <p class="abs tagline">K P Guard Services are always there, always available, wherever and whenever you need us.</p>

  <div class="abs switch-offer">
    <p class="switch-offer__lead">Not happy with your current provider? Free of charge no obligation take over survey and quotation and up to £100 off.</p>
    <p class="switch-offer__deal">£150 Discount on Installations *terms and conditions apply</p>
  </div>

  <h2 class="abs price-title" style="left:207px;top:344px;font-weight:400">Intruder Alarms</h2>
  <div class="abs price-box price-box--alarm">
    <p class="price-box__from">Installed<br>Starting From</p>
    <p class="price-box__amount">£495</p>
    <p class="price-box__plus">+</p>
    <p class="price-box__vat">VAT</p>
  </div>

  <h2 class="abs price-title" style="left:366px;top:365px;font-weight:400">CCTV Systems</h2>
  <div class="abs price-box price-box--cctv">
    <p class="price-box__from">Installed<br>Starting From</p>
    <p class="price-box__amount">£595 + VAT (based on 2 cameras)</p>
  </div>

  <div class="footer-line"></div>
  <div class="phone-tab">
    <svg width="22" height="22" viewBox="0 0 24 24" aria-hidden="true"><path d="M6.6 2.5l3 3.4-1.8 2.3c1.2 2.6 3.3 4.8 6 6l2.3-1.8 3.4 3-1.9 3.2C10.4 18.4 5.6 13.6 3.4 4.4z" fill="none" stroke="var(--ink)" stroke-width="1.3" stroke-linejoin="round"/></svg>
    <p class="phone-tab__number">01632 480913</p>
  </div>
  <ul class="contacts">
    <li><svg width="11" height="12" viewBox="0 0 12 14" aria-hidden="true"><path d="M6 13.5S1 8 1 5a5 5 0 0110 0c0 3-5 8.5-5 8.5z" fill="var(--ink)"/><circle cx="6" cy="5" r="1.8" fill="var(--white)"/></svg>14 Harlow Lane, Brentwood, Essex, CM14 9ZZ</li>
    <li><svg width="12" height="10" viewBox="0 0 14 10" aria-hidden="true"><rect x=".7" y=".7" width="12.6" height="8.6" fill="none" stroke="var(--ink)" stroke-width="1.3"/><path d="M1 1l6 5 6-5" fill="none" stroke="var(--ink)" stroke-width="1.3"/></svg>operations@kpguardservices.co.uk</li>
    <li><svg width="12" height="12" viewBox="0 0 14 14" aria-hidden="true"><g fill="none" stroke="var(--ink)" stroke-width="1"><circle cx="7" cy="7" r="6"/><ellipse cx="7" cy="7" rx="2.6" ry="6"/><path d="M1 7h12M2 4h10M2 10h10"/></g></svg>www.kpguardservices.co.uk</li>
  </ul>
</section>

<!-- Back side -->
<section class="sheet sheet--back">
  <div class="photo" style="left:0;top:0;width:512px;height:270px" role="img" aria-label="Wall-mounted security touch panel in a bright modern kitchen"></div>
  <svg class="wave" width="512" height="280" viewBox="0 0 512 280" aria-hidden="true">
    <path d="M0 180 C120 250 390 260 512 180 L512 280 L0 280 Z" fill="var(--orange)"/>
    <path d="M0 190 C120 262 390 272 512 192 L512 280 L0 280 Z" fill="var(--white)"/>
  </svg>
  <div class="abs headline-panel">
    <h1 class="headline">Are you looking to keep you and your premises safe?</h1>
  </div>
  <div class="photo" style="left:210px;top:232px;width:94px;height:78px;border-radius:8px 8px 47px 47px;background:radial-gradient(circle at 50% 60%,#3b3f45 20%,#d9dcdf 55%,#f4f4f4)" role="img" aria-label="White dome security camera"></div>

  <div class="brand" style="left:340px;top:212px;width:150px;font-size:22px">
    <span class="brand__mark" style="width:42px;height:42px;margin-bottom:8px"></span>K P GUARD<br>SERVICES
  </div>

  <ul class="points points--left">
    <li style="top:243px;width:160px">K P Guard Services install, maintain and repair all intruder alarms, CCTV, intercom and access control.</li>
    <li style="top:332px;width:200px">View, control and manage your security systems anywhere in the world.</li>
    <li style="top:393px">Feel at ease with monitoring services &amp; police response tailored to suit you and your business.</li>
    <li style="top:459px">K P Guard can takeover any existing security system and offer maintenance checks to guarantee the best performance for you and your premises.</li>
  </ul>
  <ul class="points points--right">
    <li style="top:334px">K P Guard understand that being security conscious is ever increasing, protecting your property and family is a number one priority.</li>
    <li style="top:402px">Our fully insured and accredited team offer quality, safety and cost efficiency throughout the whole process.</li>
    <li style="top:459px">K P Guard Services are using the latest cloud-based technology to stay connected with your home and business 24/7.</li>
  </ul>

  <div class="badge" style="left:18px;top:528px;width:48px;height:60px"></div>
  <div class="badge" style="left:27px;top:533px;width:30px;height:30px;border-radius:50%"></div>
  <p class="badge-label" style="left:18px;top:570px;width:48px">Intruder Alarm Systems</p>
  <div class="badge" style="left:70px;top:528px;width:40px;height:60px"></div>
  <div class="badge" style="left:136px;top:533px;width:34px;height:34px;border-radius:50%"></div>
  <p class="badge-label" style="left:133px;top:572px;width:40px">CCTV Systems</p>
  <div class="badge" style="left:190px;top:551px;width:66px;height:22px;border-radius:3px"></div>

  <p class="abs cta">If you are looking to improve the security in your home, office or commercial property then call a member of our team today for a <b>free quote.</b></p>

  <div class="footer-line" style="top:609px"></div>
  <div class="phone-tab">
    <svg width="22" height="22" viewBox="0 0 24 24" aria-hidden="true"><path d="M6.6 2.5l3 3.4-1.8 2.3c1.2 2.6 3.3 4.8 6 6l2.3-1.8 3.4 3-1.9 3.2C10.4 18.4 5.6 13.6 3.4 4.4z" fill="none" stroke="var(--ink)" stroke-width="1.3" stroke-linejoin="round"/></svg>
    <p class="phone-tab__number">01632 480913</p>
  </div>
  <ul class="contacts" style="left:200px;top:616px">
    <li><svg width="11" height="12" viewBox="0 0 12 14" aria-hidden="true"><path d="M6 13.5S1 8 1 5a5 5 0 0110 0c0 3-5 8.5-5 8.5z" fill="var(--ink)"/><circle cx="6" cy="5" r="1.8" fill="var(--white)"/></svg>14 Harlow Lane, Brentwood, Essex, CM14 9ZZ</li>
    <li><svg width="12" height="10" viewBox="0 0 14 10" aria-hidden="true"><rect x=".7" y=".7" width="12.6" height="8.6" fill="none" stroke="var(--ink)" stroke-width="1.3"/><path d="M1 1l6 5 6-5" fill="none" stroke="var(--ink)" stroke-width="1.3"/></svg>operations@kpguardservices.co.uk</li>
    <li><svg width="12" height="12" viewBox="0 0 14 14" aria-hidden="true"><g fill="none" stroke="var(--ink)" stroke-width="1"><circle cx="7" cy="7" r="6"/><ellipse cx="7" cy="7" rx="2.6" ry="6"/><path d="M1 7h12M2 4h10M2 10h10"/></g></svg>www.kpguardservices.co.uk</li>
  </ul>
</section>

</body>
</html>
```